Marlowe Scalp Clinic New Branding Stationary Set - updated Oct 30th 2017

Updated on 30th Oct 2017 as we now need a whole folder design instead of a folder cover. We have thought out exactly what should be on it so it wont be hard. We are happy for this to be completed only by the winning designer if you like. And also we are guaranteeing this project now. Thanks!

We just got our new logo and now we would like a stationary set so we can brand our company communications. The items we need designed are:
Business cards
Letterhead
Appointment confirmation cards
Folder - switched from folder cover. Note that if you don't wish to do this unless you are selected as the winner this is fine.

1. Business cards - for 5 employees, final names will be given once the winner is selected, but you can use this one as the sample:
Lucinda Prieto
Hair Regrowth Expert
Marlowe Scalp Clinic
7127 Marbury Ave, Suite 500
Kestrel Park CA 90877
lucinda@gavinthorpemd.example
(555) 238-9016

2. Letterhead 8.5" x 11.0" vertical
Marlowe Scalp Clinic
Kestrel Park CA 90877
office@haltandthicken.example
(555) 238-9016

3. Appointment Confirmation cards - business card size
Marlowe Scalp Clinic
Kestrel Park CA 90877
Appointment For:
Date:
Time:
If you are unable to make your appointment, please contact us to reschedule at:
(555) 238-9016
info@gavinthorpemd.example

*UPDATED*
4. Folder 9" x 12 " vertical with double pocket
We would like the infinity image from the logo made really big so the left side is on the back and the right side with the + sign is on the front and its takes up the maximum room on the folder.
On the front below the half logo it should say "A Biochemical Revolution..."
On the inside we would also like to have the infinity sign from the logo but faded and half on the left pocket half on the right.
On left inside pocket it should say (this will be partically written on top of the logo):
Gavin Thorpe MD
Precision Medicine
Halt and Thicken Hair
On the Right inside pocket it should say the following:
Because the Enemy of BETTER Health is Good Health
BETTER Ingredients
BETTER Recipe
BETTER Medicine
On the back below the logo on the bottom should be the contact information.
I attached a picture of our drawing of what we want for this to make it easier.

Here is our website to give you an idea of our branding: http://www.haltandthicken.example/

We are the only true cure for hair loss and need to look professional and highest quality and beyond reproach from an ethical standpoint. We are a medical clinic so this should be portrayed also.
We cured hair loss by analyzing biochemistry and rebalancing it so that the process reverses and your own hair can grow back naturally.

Business card information:

OK so here is the information for the business cards:

Lucinda Prieto
Hair Regrowth Expert
(555) 238-9016
www.haltandthicken.example

Marisol Quintero
Hair Growth Consultant
(555) 238-9016
marisol@gavinthorpemd.example
www.haltandthicken.example

Glenda Hutchins
CMO/COO
(555) 238-9016
glenda@haltandthicken.example
www.haltandthicken.example

Dr Lou Thorpe
President
(555) 238-9016
info@gavinthorpemd.example
www.haltandthicken.example

Marlowe Scalp Clinic
Customer Service
(555) 238-9016
info@gavinthorpemd.example
www.haltandthicken.example

Target Market(s)

Men aged 20-24 who care about their appearance, care about their hair and care about the world.

Industry/Entity Type

Medical And Science

Font styles to use
Sans Serif

Colors
00a990
ffffff
9d9d9d
333333

Requirements
Must have
• Must use the logo and our brand colors from the logo in all designs.
• The pantone colors are:
• Green: #4ca26f
• Light Grey: #999999
• The design should be symmetrical and balanced.
Nice to have
• It should look reasonably masculine.
Should not have
• Do not include any red in the design.

```html
<!DOCTYPE html>
<html lang="en">
<head>
<meta charset="utf-8">
<title>Visiting Card Options – Marlowe Scalp Clinic</title>
<link rel="stylesheet" href="https://fonts.googleapis.com/css2?family=Source+Sans+3:wght@400;600;700&display=swap">
<style>
  :root {
    --page-bg: #000000;
    --card-bg: #ffffff;
    --brand-green: #4ca26f;
    --brand-teal: #00a990;
    --ink-dark: #111111;
    --ink-mid: #555555;
    --ink-soft: #777777;
    --ink-light: #999999;
    --card-w: 529px;
    --card-h: 311px;
  }
  * { box-sizing: border-box; margin: 0; padding: 0; }
  html, body {
    width: 1200px;
    height: 823px;
    overflow: hidden;
    background: var(--page-bg);
    font-family: "Source Sans 3", "Source Sans Pro", sans-serif;
  }
  .sheet { position: relative; width: 1200px; height: 823px; }
  .sheet-title {
    position: absolute;
    left: 105px;
    top: 30px;
    font-size: 23px;
    font-weight: 700;
    color: var(--brand-green);
    letter-spacing: 0.2px;
  }
  .card {
    position: absolute;
    width: var(--card-w);
    height: var(--card-h);
    background: var(--card-bg);
    overflow: hidden;
  }
  .card--a { left: 70px;  top: 95px; }
  .card--b { left: 642px; top: 95px; }
  .card--c { left: 70px;  top: 451px; }
  .card--d { left: 642px; top: 451px; }

  .card__person { position: absolute; left: 35px; top: 50px; line-height: 1.22; }
  .card__name { font-size: 31px; font-weight: 700; color: var(--brand-green); line-height: 1.15; }
  .card__role { font-size: 18px; font-weight: 600; color: var(--ink-mid); }
  .card__contact { font-size: 18px; font-weight: 400; color: var(--ink-soft); }

  .card__office {
    position: absolute;
    right: 47px;
    top: 205px;
    text-align: right;
    line-height: 1.25;
  }
  .card__company { font-size: 17px; font-weight: 600; color: var(--brand-green); text-transform: uppercase; }
  .card__address { font-size: 17px; color: var(--ink-soft); }

  /* Option B: dark name, teal company */
  .card--b .card__person { top: 52px; line-height: 1.32; }
  .card--b .card__name { color: var(--ink-dark); font-size: 28px; line-height: 1.2; }
  .card--b .card__role { font-size: 16px; }
  .card--b .card__contact { font-size: 16px; color: var(--ink-light); }
  .card--b .card__office { right: 29px; top: 216px; line-height: 1.3; }
  .card--b .card__company { font-size: 15px; color: var(--brand-teal); }
  .card--b .card__address { font-size: 15px; color: var(--ink-light); }

  /* Option C: smaller office block */
  .card--c .card__office { top: 204px; line-height: 1.3; }
  .card--c .card__company,
  .card--c .card__address { font-size: 15px; }

  /* Option D: compact throughout */
  .card--d .card__person { top: 55px; line-height: 1.25; }
  .card--d .card__name { font-size: 28px; line-height: 1.15; }
  .card--d .card__role,
  .card--d .card__contact { font-size: 16px; }
  .card--d .card__office { top: 204px; line-height: 1.3; }
  .card--d .card__company,
  .card--d .card__address { font-size: 15px; }
</style>
</head>
<body>
<main class="sheet">
  <h1 class="sheet-title">VISITING CARD OPTIONS</h1>

  <section class="card card--a">
    <div class="card__person">
      <p class="card__name">Lucinda Prieto</p>
      <p class="card__role">Hair Regrowth Expert</p>
      <p class="card__contact">lucinda@gavinthorpemd.example</p>
      <p class="card__contact">(555) 238-9016</p>
    </div>
    <div class="card__office">
      <p class="card__company">Marlowe Scalp Clinic</p>
      <p class="card__address">7127 Marbury Ave, Suite 500</p>
      <p class="card__address">Kestrel Park CA 90877</p>
    </div>
  </section>

  <section class="card card--b">
    <div class="card__person">
      <p class="card__name">Lucinda Prieto</p>
      <p class="card__role">Hair Regrowth Expert</p>
      <p class="card__contact">lucinda@gavinthorpemd.example</p>
      <p class="card__contact">(555) 238-9016</p>
    </div>
    <div class="card__office">
      <p class="card__company">Marlowe Scalp Clinic</p>
      <p class="card__address">7127 Marbury Ave, Suite 500</p>
      <p class="card__address">Kestrel Park CA 90877</p>
    </div>
  </section>

  <section class="card card--c">
    <div class="card__person">
      <p class="card__name">Lucinda Prieto</p>
      <p class="card__role">Hair Regrowth Expert</p>
      <p class="card__contact">lucinda@gavinthorpemd.example</p>
      <p class="card__contact">(555) 238-9016</p>
    </div>
    <div class="card__office">
      <p class="card__company">Marlowe Scalp Clinic</p>
      <p class="card__address">7127 Marbury Ave, Suite 500</p>
      <p class="card__address">Kestrel Park CA 90877</p>
    </div>
  </section>

  <section class="card card--d">
    <div class="card__person">
      <p class="card__name">Lucinda Prieto</p>
      <p class="card__role">Hair Regrowth Expert</p>
      <p class="card__contact">lucinda@gavinthorpemd.example</p>
      <p class="card__contact">(555) 238-9016</p>
    </div>
    <div class="card__office">
      <p class="card__company">Marlowe Scalp Clinic</p>
      <p class="card__address">7127 Marbury Ave, Suite 500</p>
      <p class="card__address">Kestrel Park CA 90877</p>
    </div>
  </section>
</main>
</body>
</html>
```